Wine Label for a Sweet Wine Called "Glimmo"

We need a wine label that will be used for both a sweet red and a sweet white wine. The very important thing to remember is the target market for these wines is: young American women who love sweet wines and they also spend a lot of their money on their hair, clothes, jewelry, nails. They LOVE Glimmo (Glimmo is a word used to describe flashy accessories, jewelry, decoration.) This label needs to be eye catching, showy, fun, glittery. Please put the brand name, "Glimmo," big, and then in smaller but still readable words underneath the label or somewhere on the label: Sweet, Sophisticated, Red (or white). (An example of what I mean is attached). To differentiate between the two color wines you can suggest color changes to differentiate between the red label and the white label but the label design itself should be the same. Ultimately, the label can be the exact same label for both white and red as long as it looks good on a white wine (a greenish/yellow wine in a clear glass bottle) and a red wine (a dark color wine in a dark bottle).

I've attached an example of the text size relationship between the word Glimmo and the words to go underneath or elsewhere on the label, but you can certainly play with this-- it is just a suggestion of the text size relationship, and definitely NOT at all mandatory that you use any of these fonts.

You can pick the size of the label but try to stay within normal wine label sizes, meaning don't go bigger than approx. 3.5 inches wide and 5 inches tall.

Target Market(s)

Young American women who love sweet wines and spend a lot of money on their hair, clothes, jewelry, nails. They love Glimmo (Glimmo is a word that means flashy accessories, jewelry, decoration)

Requirements
Must have
• It needs to be flashy, glittery, fun, eye catching, memorable
Nice to have
• It shouldn't be too too ultra feminine! The target market is strong independent women and we also have men who will buy it too.

```html
<!DOCTYPE html>
<html lang="en">
<head>
<meta charset="utf-8">
<title>Glimmo — Wine Label</title>
<link rel="stylesheet" href="https://fonts.googleapis.com/css2?family=Marcellus&family=Lato:wght@400&display=swap">
<style>
  :root {
    --backdrop: #2a2b2b;
    --label-dark: #1e1f21;
    --label-line: #26272a;
    --silver-light: #f2f2f2;
    --silver-mid: #c9c9c9;
    --silver-dark: #a9a9a9;
    --wordmark: #dcdcdc;
    --gold: #c9a233;
    --wine-red: #8c1c2e;
  }
  * { box-sizing: border-box; margin: 0; padding: 0; }
  html, body {
    width: 752px;
    height: 1200px;
    overflow: hidden;
    background: var(--backdrop);
  }
  .canvas {
    position: relative;
    width: 752px;
    height: 1200px;
  }
  .label {
    position: absolute;
    left: 56px;
    top: 348px;
    width: 640px;
    height: 504px;
  }
  .label-body {
    position: absolute;
    inset: 0 0 64px 0;
    background:
      repeating-linear-gradient(to bottom, var(--label-line) 0 1px, var(--label-dark) 1px 4px),
      var(--label-dark);
  }
  .brand {
    position: absolute;
    left: 0;
    right: 0;
    top: 150px;
    text-align: center;
  }
  .brand-dot {
    display: block;
    width: 22px;
    height: 22px;
    margin: 0 auto 36px;
    border-radius: 50%;
    background: var(--gold);
  }
  .brand-name {
    font-family: "Marcellus", serif;
    font-weight: 400;
    font-size: 104px;
    line-height: 1;
    letter-spacing: 0.16em;
    padding-left: 0.16em;
    color: var(--wordmark);
  }
  .tag-strip {
    position: absolute;
    left: 0;
    right: 0;
    bottom: 0;
    height: 72px;
  }
  .tag-strip svg {
    position: absolute;
    inset: 0;
    width: 100%;
    height: 100%;
  }
  .tagline {
    position: absolute;
    left: 0;
    right: 0;
    top: 34px;
    text-align: center;
    font-family: "Lato", sans-serif;
    font-size: 14px;
    letter-spacing: 0.3em;
    color: var(--wine-red);
    text-transform: uppercase;
  }
  .tagline .divider {
    margin: 0 0.6em;
  }
</style>
</head>
<body>
<main class="canvas">
  <section class="label" aria-label="Glimmo wine label">
    <div class="label-body">
      <div class="brand">
        <span class="brand-dot" aria-hidden="true"></span>
        <h1 class="brand-name">GLIMMO</h1>
      </div>
    </div>
    <div class="tag-strip">
      <svg viewBox="0 0 640 72" preserveAspectRatio="none" aria-hidden="true">
        <defs>
          <linearGradient id="silver" x1="0" y1="0" x2="1" y2="0">
            <stop offset="0" stop-color="var(--silver-dark)"/>
            <stop offset="0.5" stop-color="var(--silver-light)"/>
            <stop offset="1" stop-color="var(--silver-mid)"/>
          </linearGradient>
        </defs>
        <path fill="url(#silver)" d="M0 14 L20 6 L40 14 L60 6 L80 14 L100 6 L120 14 L140 6 L160 14 L180 6 L200 14 L220 6 L240 14 L260 6 L280 14 L300 6 L320 14 L340 6 L360 14 L380 6 L400 14 L420 6 L440 14 L460 6 L480 14 L500 6 L520 14 L540 6 L560 14 L580 6 L600 14 L620 6 L640 14 L640 72 L0 72 Z"/>
      </svg>
      <p class="tagline">Sweet<span class="divider">|</span>Sophisticated<span class="divider">|</span>Red</p>
    </div>
  </section>
</main>
</body>
</html>
```